Tavlor Suite Background image creation.

We need someone to develop an image that is 1920x1080 using our company logo and and colors. We will be using this as the login page background on tavlorsuite.net for all our clients.

```html
<!DOCTYPE html>
<html lang="en">
<head>
<meta charset="utf-8">
<title>Corvane Networks – Sign in</title>
<link rel="stylesheet" href="https://fonts.googleapis.com/css2?family=Open+Sans:ital,wght@0,400;0,600;1,400&display=swap">
<style>
  :root {
    --bg-cyan: #17d3ea;
    --bg-sky: #5ec3e6;
    --bg-blue: #3f86cc;
    --bg-indigo: #4a4fbf;
    --white: #ffffff;
    --field-icon: #8a8f99;
    --placeholder: #9aa0a8;
    --button: #367dc0;
    --button-text: #f2f6fb;
  }
  * { box-sizing: border-box; margin: 0; padding: 0; }
  html, body { width: 1200px; height: 675px; overflow: hidden; }
  body { font-family: "Open Sans", sans-serif; }
  .login-screen { position: relative; width: 1200px; height: 675px; overflow: hidden; }
  .backdrop {
    position: absolute; inset: 0;
    background:
      linear-gradient(200deg, rgba(74,79,191,0.9) 0%, rgba(74,79,191,0) 40%),
      linear-gradient(20deg, var(--bg-cyan) 0%, var(--bg-sky) 35%, var(--bg-blue) 70%, var(--bg-indigo) 100%);
  }
  .brand {
    position: absolute; left: 457px; top: 172px; width: 300px; height: 118px;
    display: flex; align-items: center; gap: 22px;
  }
  .brand-mark { width: 80px; height: 80px; border-radius: 50%; background: var(--white); flex: none; }
  .brand-name { color: var(--white); font-weight: 600; line-height: 1; }
  .brand-name .primary { display: block; font-size: 36px; }
  .brand-name .secondary { display: block; font-size: 15px; letter-spacing: 9px; margin-top: 4px; }
  .login-form { position: absolute; left: 445px; top: 315px; width: 310px; }
  .field {
    height: 46px; background: var(--white); border-radius: 3px;
    display: flex; align-items: center; margin-bottom: 14px;
  }
  .field svg { width: 16px; height: 16px; margin-left: 14px; flex: none; fill: var(--field-icon); }
  .field span { margin-left: 26px; color: var(--placeholder); font-size: 15px; }
  .field .mask { font-size: 13px; letter-spacing: 1px; }
  .login-button {
    margin-top: 2px; height: 32px; background: var(--button);
    color: var(--button-text); font-size: 14px; display: flex; align-items: center; justify-content: center;
  }
  .form-options {
    display: flex; justify-content: space-between; align-items: center;
    margin-top: 18px; padding: 0 10px 0 9px; color: var(--white); font-size: 13px;
  }
  .remember { display: flex; align-items: center; gap: 9px; }
  .checkbox { width: 14px; height: 14px; background: var(--white); border-radius: 3px; }
  .forgot { font-style: italic; }
</style>
</head>
<body>
<main class="login-screen">
  <div class="backdrop" role="img" aria-label="Geometric triangle pattern background in cyan to indigo blues"></div>

  <div class="brand">
    <div class="brand-mark"></div>
    <div class="brand-name">
      <span class="primary">Corvane</span>
      <span class="secondary">Networks</span>
    </div>
  </div>

  <form class="login-form">
    <div class="field">
      <svg viewBox="0 0 16 16" aria-hidden="true"><circle cx="8" cy="4.5" r="3.5"/><path d="M1 16c0-4 3-6.5 7-6.5s7 2.5 7 6.5z"/></svg>
      <span>Username</span>
    </div>
    <div class="field">
      <svg viewBox="0 0 16 16" aria-hidden="true"><path d="M4.5 7V5a3.5 3.5 0 0 1 7 0v2h-1.6V5a1.9 1.9 0 0 0-3.8 0v2z"/><rect x="2.5" y="7" width="11" height="8" rx="1"/></svg>
      <span class="mask">*******</span>
    </div>
    <div class="login-button">LOGIN</div>
    <div class="form-options">
      <div class="remember"><div class="checkbox"></div><span>Remember me</span></div>
      <span class="forgot">Forgot Password?</span>
    </div>
  </form>
</main>
</body>
</html>
```